Garlic Farm for Farm Sales/Restaurant sales

Need a professional, but appealing to agriculture world. We are selling 27 kinds of Organic Garlic from a farm in Simla,CO. I have uploaded logo and business information-we are going to need a template, because I will need to use it for four separate people.
-We are trying to appeal to Farm to table restaurants
-As well as growers/farmers

Target Market(s)

Agriculture Sales/Restaurants-Organic

Industry/Entity Type

Agriculture

Contact Information for Business Card

Want it to look more unique then your average orbel mart card- I want it to look amazing

Font styles to use
Sans Serif

Colors
0455a3
ec1f27
fbed22
ffffff

Requirements
Must have
• Just be creative
Nice to have
• Colorful
Should not have
• plain

```html
<!DOCTYPE html>
<html lang="en">
<head>
<meta charset="utf-8">
<title>Summit Clove Farm – Business Card</title>
<link href="https://fonts.googleapis.com/css2?family=Arimo:wght@400;700&display=swap" rel="stylesheet">
<style>
  :root {
    --navy: #0d2f5f;
    --red: #c8102e;
    --yellow: #fdd700;
    --paper: #f4f3ef;
    --ink: #1f3b66;
    --backdrop: #ece8e1;
  }
  * { margin: 0; padding: 0; box-sizing: border-box; }
  html, body { width: 1004px; height: 1200px; overflow: hidden; }
  body {
    background: var(--backdrop);
    font-family: "Arimo", Arial, sans-serif;
    position: relative;
  }
  .card { position: absolute; }
  .card svg.card-art { position: absolute; inset: 0; display: block; }
  .card-front { left: 99px; top: 115px; width: 755px; height: 449px; }
  .card-back { left: 141px; top: 628px; width: 758px; height: 449px; }

  .brand-name {
    position: absolute;
    color: var(--navy);
    font-weight: 700;
    white-space: nowrap;
    transform: translateX(-50%);
  }
  .card-front .brand-name { left: 444px; top: 238px; font-size: 46px; }
  .card-back .brand-name { left: 505px; top: 112px; font-size: 22px; }

  .holder { position: absolute; left: 97px; top: 150px; color: var(--ink); }
  .holder-name { font-size: 26px; font-weight: 700; line-height: 32px; }
  .holder-role { font-size: 23px; line-height: 30px; }

  .contact-list { position: absolute; left: 97px; top: 220px; list-style: none; }
  .contact-list li {
    display: flex; align-items: center;
    height: 34.5px;
    font-size: 20px; color: var(--ink);
  }
  .contact-list svg { width: 22px; height: 22px; margin-right: 20px; flex: none; }
</style>
</head>
<body>

<!-- Front of card -->
<section class="card card-front" aria-label="Business card front">
  <svg class="card-art" width="755" height="449" viewBox="0 0 755 449">
    <defs>
      <clipPath id="front-shape">
        <path d="M0 0 H680 Q755 0 755 75 V449 H80 Q0 449 0 369 Z"/>
      </clipPath>
      <path id="band-curve" d="M0 0 H150 C100 50 80 150 90 240 C100 340 190 420 330 449 H0 Z"/>
    </defs>
    <g clip-path="url(#front-shape)">
      <rect width="755" height="449" fill="var(--paper)"/>
      <path d="M150 0 C100 50 80 150 90 240 C100 340 190 420 330 449" transform="translate(34,0)" fill="none" stroke="var(--navy)" stroke-width="4"/>
      <use href="#band-curve" transform="translate(26,0)" fill="var(--yellow)"/>
      <use href="#band-curve" transform="translate(14,0)" fill="var(--red)"/>
      <use href="#band-curve" fill="var(--navy)"/>
    </g>
    <circle cx="444" cy="146" r="62" fill="var(--red)"/>
  </svg>
  <div class="brand-name">Summit Clove Farm</div>
</section>

<!-- Back of card -->
<section class="card card-back" aria-label="Business card back">
  <svg class="card-art" width="758" height="449" viewBox="0 0 758 449">
    <defs>
      <clipPath id="back-shape">
        <path d="M80 0 H758 V369 Q758 449 678 449 H0 V80 Q0 0 80 0 Z"/>
      </clipPath>
    </defs>
    <g clip-path="url(#back-shape)">
      <rect width="758" height="449" fill="var(--paper)"/>
      <g transform="translate(758,0) scale(-1,1)">
        <path d="M150 0 C100 50 80 150 90 240 C100 340 190 420 330 449" transform="translate(34,0)" fill="none" stroke="var(--navy)" stroke-width="4"/>
        <use href="#band-curve" transform="translate(26,0)" fill="var(--yellow)"/>
        <use href="#band-curve" transform="translate(14,0)" fill="var(--red)"/>
        <use href="#band-curve" fill="var(--navy)"/>
      </g>
    </g>
    <circle cx="508" cy="68" r="34" fill="var(--red)"/>
  </svg>
  <div class="brand-name">Summit Clove Farm</div>

  <div class="holder">
    <p class="holder-name">Your Name</p>
    <p class="holder-role">Position</p>
  </div>

  <ul class="contact-list">
    <li>
      <svg viewBox="0 0 24 24" aria-hidden="true"><path d="M6.5 3 L9.5 3 L10.5 8 L8.3 9.6 C9.5 12.3 11.7 14.5 14.4 15.7 L16 13.5 L21 14.5 L21 17.5 C21 19.5 19.5 21 17.5 21 C9.5 20.5 3.5 14.5 3 6.5 C3 4.5 4.5 3 6.5 3 Z" fill="var(--red)"/></svg>
      123-456-7890
    </li>
    <li>
      <svg viewBox="0 0 24 24" aria-hidden="true"><rect x="6" y="2.5" width="12" height="19" rx="2" fill="none" stroke="var(--red)" stroke-width="2"/><circle cx="12" cy="18" r="1.2" fill="var(--red)"/></svg>
      123-456-7888
    </li>
    <li>
      <svg viewBox="0 0 24 24" aria-hidden="true"><rect x="3" y="6" width="18" height="12" fill="none" stroke="var(--red)" stroke-width="2"/><path d="M3 6 L12 13 L21 6" fill="none" stroke="var(--red)" stroke-width="2"/></svg>
      name@companyname.com
    </li>
    <li>
      <svg viewBox="0 0 24 24" aria-hidden="true"><circle cx="12" cy="12" r="9" fill="none" stroke="var(--red)" stroke-width="2"/><ellipse cx="12" cy="12" rx="4" ry="9" fill="none" stroke="var(--red)" stroke-width="1.6"/><path d="M3 12 H21 M5 7.5 H19 M5 16.5 H19" stroke="var(--red)" stroke-width="1.6"/></svg>
      www.companyname.com
    </li>
    <li>
      <svg viewBox="0 0 24 24" aria-hidden="true"><path d="M12 2 C8 2 5 5 5 9 C5 14 12 22 12 22 C12 22 19 14 19 9 C19 5 16 2 12 2 Z" fill="var(--red)"/><circle cx="12" cy="9" r="2.8" fill="var(--paper)"/></svg>
      address
    </li>
  </ul>
</section>

</body>
</html>
```